social interest sharing site needs a web site design

we need a web site design for a social web platform.
the site is one page(main page), that is split into 3 sections
each section is a different color(red,green and blue)
and a user can choose to share each of the sections.
any section/color will contain boxes , each box can contain different media types.

the media types:
* list of URLS
* list of articles including title + image + description
* list of videos
* thumbnails of images
* calender
* list of emails

the main content will look like quiltboard layout
multiple boxes each box can contain different type of content as described above

each color is a different tab
each tab will have layout like quiltboard
Updates

please read the last description update.
and i uploaded an image that can explain the requirements better

thanks
Oren

```html
<!DOCTYPE html>
<html lang="en">
<head>
<meta charset="utf-8">
<title>Huebox.me</title>
<link href="https://fonts.googleapis.com/css2?family=Oswald:wght@400;500&family=Open+Sans:wght@400;600&display=swap" rel="stylesheet">
<style>
:root{
  --red:#dd6a5c;
  --teal:#00aba4;
  --navy:#3d5679;
  --dark:#3a3a3a;
  --header:#e3e4e3;
  --card:#ffffff;
  --muted:#9a9a9a;
  --text:#6e6e6e;
  --accent:#c8a45a;
}
*{box-sizing:border-box;margin:0;padding:0}
html,body{width:836px;height:1200px;overflow:hidden}
body{font-family:"Open Sans",Arial,sans-serif;background:var(--header);position:relative}
.site-header{position:absolute;left:0;top:0;width:836px;height:73px;background:var(--header)}
.brand{position:absolute;left:67px;top:20px;display:flex;align-items:center;gap:8px}
.brand-mark{width:14px;height:14px;background:var(--dark)}
.brand-name{font-family:"Oswald",sans-serif;font-weight:400;font-size:26px;line-height:32px;color:var(--dark)}
.nav{position:absolute;top:34px;left:320px;display:flex}
.nav a{font-family:"Oswald",sans-serif;font-size:13px;color:#333;text-decoration:none;height:21px;line-height:21px;padding:0 12px;letter-spacing:.5px}
.nav a.active{background:var(--dark);color:#fff;border-radius:2px;width:56px;text-align:center;padding:0}
.nav a.qv{margin-left:7px}
.login{position:absolute;left:579px;top:35px;width:56px;height:21px;background:var(--red);color:#fff;font-family:"Oswald",sans-serif;font-size:12px;line-height:21px;text-align:center;border-radius:2px}
.search{position:absolute;left:649px;top:35px;width:123px;height:21px;background:#fff;border-radius:2px;font-size:8px;color:#999;line-height:21px;padding-left:13px}
.search .go{position:absolute;right:0;top:0;width:20px;height:21px;background:var(--red);border-radius:0 2px 2px 0}
.pointer{position:absolute;left:396px;top:73px;width:0;height:0;border-left:10px solid transparent;border-right:10px solid transparent;border-top:8px solid var(--header);z-index:2}

.band{position:absolute;left:0;width:836px;height:376px}
.band.red{top:73px;background:var(--red)}
.band.teal{top:449px;background:var(--teal)}
.band.navy{top:825px;height:375px;background:var(--navy)}

.share{position:absolute;left:691px;top:9px;width:80px;height:23px;background:#fff;display:flex;font-size:6px;color:#555;box-shadow:0 1px 2px rgba(0,0,0,.2)}
.share .s{background:var(--dark);color:#fff;width:40px;display:flex;align-items:center;justify-content:center;gap:3px}
.share .l{flex:1;display:flex;align-items:center;justify-content:center;gap:2px}

.card{position:absolute;background:var(--card);box-shadow:0 1px 3px rgba(0,0,0,.25)}
.card h3{font-family:"Oswald",sans-serif;font-weight:400;font-size:11px;color:#333;letter-spacing:.2px}
.card-head{display:flex;justify-content:space-between;align-items:center;margin:0 7px;padding:9px 8px 4px;border-bottom:1px dashed #ccc}
.ico{width:9px;height:8px;background:#555;border-radius:1px}
.meta{position:absolute;bottom:7px;left:8px;right:8px;display:flex;justify-content:space-between;font-size:6px;color:var(--muted)}
.meta .n{display:flex;gap:5px;align-items:center}
.heart{width:7px;height:6px;background:#999;border-radius:3px 3px 1px 1px}
.bubble{width:6px;height:5px;background:#999}

.featured{left:67px;top:51px;width:276px;height:267px}
.featured .photo{height:205px;background:linear-gradient(160deg,#4a3d2f 0%,#8a6a45 40%,#c9a878 70%,#d9c29c 100%)}
.ribbon{position:absolute;left:0;top:0;width:60px;height:60px;overflow:hidden}
.ribbon::before{content:"";position:absolute;left:0;top:0;border-top:60px solid #2b2b2b;border-right:60px solid transparent}
.ribbon span{position:absolute;left:2px;top:16px;transform:rotate(-45deg);font-family:"Oswald",sans-serif;font-size:8px;color:#fff}
.featured .body{padding:7px 12px 0}
.featured .title{display:flex;justify-content:space-between;border-bottom:1px dashed #ccc;padding-bottom:2px}
.socials{display:flex;gap:2px}
.socials i{width:8px;height:8px;background:#444;display:block}
.featured p{font-size:6px;color:var(--text);line-height:8.5px;margin-top:3px}

.list{margin:6px 7px 0}
.item{display:flex;gap:6px;padding:4px 5px;border-bottom:1px solid #e6e6e6;height:35px}
.item:last-child{border-bottom:0}
.thumb{width:30px;height:28px;flex:none;background:linear-gradient(135deg,#f3b23a,#e8e0d0)}
.thumb.alt{background:linear-gradient(135deg,#3b5d8a,#e4e4e4)}
.item div{font-size:6px;line-height:8.5px;color:var(--muted)}
.item b{display:block;font-weight:600;color:var(--accent)}

.dl1{left:353px;top:51px;width:132px;height:162px}
.video{left:353px;top:222px;width:132px;height:99px;padding:6px}
.video .frame{position:relative;height:87px;background:linear-gradient(120deg,#5d4a36,#c9a070 55%,#efe6d8)}
.play{position:absolute;left:52px;top:30px;width:22px;height:22px;border-radius:50%;background:rgba(40,40,40,.8)}
.play::after{content:"";position:absolute;left:8px;top:6px;border-left:8px solid #fff;border-top:5px solid transparent;border-bottom:5px solid transparent}
.bar{position:absolute;left:0;right:0;bottom:0;height:7px;background:#333}
.bar::after{content:"";position:absolute;left:14px;right:24px;top:3px;height:1px;background:#888}

.blog{left:496px;top:51px;width:131px;height:263px}
.blog .text{margin:6px 9px 0;font-size:6px;line-height:9.4px;color:var(--text)}
.dl2{left:640px;top:51px;width:131px;height:267px}

.more{position:absolute;left:723px;top:340px;font-family:"Oswald",sans-serif;font-size:10px;color:#fff}
</style>
</head>
<body>
<header class="site-header">
  <div class="brand"><span class="brand-mark"></span><span class="brand-name">Huebox.me</span></div>
  <nav class="nav"><a class="active" href="#">HOME</a><a class="qv" href="#">QUICK VIEW</a><a href="#">UPLOAD</a></nav>
  <div class="login">Login</div>
  <div class="search">Search...<span class="go"></span></div>
</header>
<div class="pointer"></div>

<section class="band red">
  <div class="share"><span class="s">&lt; SHARE</span><span class="l">LIKE</span></div>
  <article class="card featured">
    <div class="photo" role="img" aria-label="Featured post photograph"></div>
    <div class="ribbon"><span>FEATURED</span></div>
    <div class="body"><div class="title"><h3>FEATURED POST</h3><div class="socials"><i></i><i></i><i></i></div></div>
    <p>Lorem ipsum dolor sit amet, consectetur adipisicing elit, sed do eiusmod tempor incididunt ut labore et dolore magna aliqua.</p></div>
    <div class="meta"><span>3 days ago</span><span class="n"><i class="heart"></i>122<i class="bubble"></i>1</span></div>
  </article>
  <article class="card dl1">
    <div class="card-head"><h3>DOWNLOAD NOW</h3><i class="ico"></i></div>
    <div class="list">
      <div class="item"><span class="thumb" role="img" aria-label="Download thumbnail"></span><div><b>Aliquam congue</b>Fermentum nisl. Mauris accumsan nulla vel diam.</div></div>
      <div class="item"><span class="thumb alt" role="img" aria-label="Download thumbnail"></span><div><b>Aliquam congue</b>Fermentum nisl. Mauris accumsan nulla vel diam.</div></div>
      <div class="item"><span class="thumb" role="img" aria-label="Download thumbnail"></span><div><b>Aliquam congue</b>Fermentum nisl. Mauris accumsan nulla vel diam.</div></div>
    </div>
    <div class="meta"><span>3 days ago</span><span class="n"><i class="heart"></i>122<i class="bubble"></i>1</span></div>
  </article>
  <article class="card video"><div class="frame" role="img" aria-label="Video still"><span class="play"></span><span class="bar"></span></div></article>
  <article class="card blog">
    <div class="card-head"><h3>BLOG POST</h3><i class="ico"></i></div>
    <p class="text">Lorem ipsum dolor sit amet, consectetur adipisicing elit, sed do eiusmod tempor incididunt ut labore et dolore magna aliqua. Lorem ipsum dolor sit amet, consectetur adipisicing elit, sed do eiusmod tempor incididunt ut labore et dolore magna aliqua. Lorem ipsum dolor sit amet, consectetur adipisicing elit, sed do eiusmod tempor incididunt ut labore et dolore magna aliqua. Lorem ipsum dolor sit amet, consectetur adipisicing elit, sed do eiusmod tempor incididunt ut labore et dolore magna aliqua. Lorem ipsum dolor sit amet, consectetur adipisicing elit, sed do eiusmod tempor incididunt ut labore et dolore magna aliqua.</p>
    <div class="meta"><span>3 days ago</span><span class="n"><i class="heart"></i>122<i class="bubble"></i>1</span></div>
  </article>
  <article class="card dl2">
    <div class="card-head"><h3>DOWNLOAD NOW</h3><i class="ico"></i></div>
    <div class="list">
      <div class="item"><span class="thumb" role="img" aria-label="Download thumbnail"></span><div><b>Aliquam congue</b>Fermentum nisl. Mauris accumsan nulla vel diam.</div></div>
      <div class="item"><span class="thumb alt" role="img" aria-label="Download thumbnail"></span><div><b>Aliquam congue</b>Fermentum nisl. Mauris accumsan nulla vel diam.</div></div>
      <div class="item"><span class="thumb" role="img" aria-label="Download thumbnail"></span><div><b>Aliquam congue</b>Fermentum nisl. Mauris accumsan nulla vel diam.</div></div>
      <div class="item"><span class="thumb alt" role="img" aria-label="Download thumbnail"></span><div><b>Aliquam congue</b>Fermentum nisl. Mauris accumsan nulla vel diam.</div></div>
      <div class="item"><span class="thumb" role="img" aria-label="Download thumbnail"></span><div><b>Aliquam congue</b>Fermentum nisl. Mauris accumsan nulla vel diam.</div></div>
      <div class="item"><span class="thumb alt" role="img" aria-label="Download thumbnail"></span><div><b>Aliquam congue</b>Fermentum nisl. Mauris accumsan nulla vel diam.</div></div>
    </div>
    <div class="meta"><span>3 days ago</span><span class="n"><i class="heart"></i>122<i class="bubble"></i>1</span></div>
  </article>
  <div class="more">LOAD MORE +</div>
</section>

<section class="band teal">
  <div class="share"><span class="s">&lt; SHARE</span><span class="l">LIKE</span></div>
  <article class="card featured">
    <div class="photo" role="img" aria-label="Featured post photograph"></div>
    <div class="ribbon"><span>FEATURED</span></div>
    <div class="body"><div class="title"><h3>FEATURED POST</h3><div class="socials"><i></i><i></i><i></i></div></div>
    <p>Lorem ipsum dolor sit amet, consectetur adipisicing elit, sed do eiusmod tempor incididunt ut labore et dolore magna aliqua.</p></div>
    <div class="meta"><span>3 days ago</span><span class="n"><i class="heart"></i>122<i class="bubble"></i>1</span></div>
  </article>
  <article class="card dl1">
    <div class="card-head"><h3>DOWNLOAD NOW</h3><i class="ico"></i></div>
    <div class="list">
      <div class="item"><span class="thumb" role="img" aria-label="Download thumbnail"></span><div><b>Aliquam congue</b>Fermentum nisl. Mauris accumsan nulla vel diam.</div></div>
      <div class="item"><span class="thumb alt" role="img" aria-label="Download thumbnail"></span><div><b>Aliquam congue</b>Fermentum nisl. Mauris accumsan nulla vel diam.</div></div>
      <div class="item"><span class="thumb" role="img" aria-label="Download thumbnail"></span><div><b>Aliquam congue</b>Fermentum nisl. Mauris accumsan nulla vel diam.</div></div>
    </div>
    <div class="meta"><span>3 days ago</span><span class="n"><i class="heart"></i>122<i class="bubble"></i>1</span></div>
  </article>
  <article class="card video"><div class="frame" role="img" aria-label="Video still"><span class="play"></span><span class="bar"></span></div></article>
  <article class="card blog">
    <div class="card-head"><h3>BLOG POST</h3><i class="ico"></i></div>
    <p class="text">Lorem ipsum dolor sit amet, consectetur adipisicing elit, sed do eiusmod tempor incididunt ut labore et dolore magna aliqua. Lorem ipsum dolor sit amet, consectetur adipisicing elit, sed do eiusmod tempor incididunt ut labore et dolore magna aliqua. Lorem ipsum dolor sit amet, consectetur adipisicing elit, sed do eiusmod tempor incididunt ut labore et dolore magna aliqua. Lorem ipsum dolor sit amet, consectetur adipisicing elit, sed do eiusmod tempor incididunt ut labore et dolore magna aliqua. Lorem ipsum dolor sit amet, consectetur adipisicing elit, sed do eiusmod tempor incididunt ut labore et dolore magna aliqua.</p>
    <div class="meta"><span>3 days ago</span><span class="n"><i class="heart"></i>122<i class="bubble"></i>1</span></div>
  </article>
  <article class="card dl2">
    <div class="card-head"><h3>DOWNLOAD NOW</h3><i class="ico"></i></div>
    <div class="list">
      <div class="item"><span class="thumb" role="img" aria-label="Download thumbnail"></span><div><b>Aliquam congue</b>Fermentum nisl. Mauris accumsan nulla vel diam.</div></div>
      <div class="item"><span class="thumb alt" role="img" aria-label="Download thumbnail"></span><div><b>Aliquam congue</b>Fermentum nisl. Mauris accumsan nulla vel diam.</div></div>
      <div class="item"><span class="thumb" role="img" aria-label="Download thumbnail"></span><div><b>Aliquam congue</b>Fermentum nisl. Mauris accumsan nulla vel diam.</div></div>
      <div class="item"><span class="thumb alt" role="img" aria-label="Download thumbnail"></span><div><b>Aliquam congue</b>Fermentum nisl. Mauris accumsan nulla vel diam.</div></div>
      <div class="item"><span class="thumb" role="img" aria-label="Download thumbnail"></span><div><b>Aliquam congue</b>Fermentum nisl. Mauris accumsan nulla vel diam.</div></div>
      <div class="item"><span class="thumb alt" role="img" aria-label="Download thumbnail"></span><div><b>Aliquam congue</b>Fermentum nisl. Mauris accumsan nulla vel diam.</div></div>
    </div>
    <div class="meta"><span>3 days ago</span><span class="n"><i class="heart"></i>122<i class="bubble"></i>1</span></div>
  </article>
  <div class="more">LOAD MORE +</div>
</section>

<section class="band navy">
  <div class="share"><span class="s">&lt; SHARE</span><span class="l">LIKE</span></div>
  <article class="card featured">
    <div class="photo" role="img" aria-label="Featured post photograph"></div>
    <div class="ribbon"><span>FEATURED</span></div>
    <div class="body"><div class="title"><h3>FEATURED POST</h3><div class="socials"><i></i><i></i><i></i></div></div>
    <p>Lorem ipsum dolor sit amet, consectetur adipisicing elit, sed do eiusmod tempor incididunt ut labore et dolore magna aliqua.</p></div>
    <div class="meta"><span>3 days ago</span><span class="n"><i class="heart"></i>122<i class="bubble"></i>1</span></div>
  </article>
  <article class="card dl1">
    <div class="card-head"><h3>DOWNLOAD NOW</h3><i class="ico"></i></div>
    <div class="list">
      <div class="item"><span class="thumb" role="img" aria-label="Download thumbnail"></span><div><b>Aliquam congue</b>Fermentum nisl. Mauris accumsan nulla vel diam.</div></div>
      <div class="item"><span class="thumb alt" role="img" aria-label="Download thumbnail"></span><div><b>Aliquam congue</b>Fermentum nisl. Mauris accumsan nulla vel diam.</div></div>
      <div class="item"><span class="thumb" role="img" aria-label="Download thumbnail"></span><div><b>Aliquam congue</b>Fermentum nisl. Mauris accumsan nulla vel diam.</div></div>
    </div>
    <div class="meta"><span>3 days ago</span><span class="n"><i class="heart"></i>122<i class="bubble"></i>1</span></div>
  </article>
  <article class="card video"><div class="frame" role="img" aria-label="Video still"><span class="play"></span><span class="bar"></span></div></article>
  <article class="card blog">
    <div class="card-head"><h3>BLOG POST</h3><i class="ico"></i></div>
    <p class="text">Lorem ipsum dolor sit amet, consectetur adipisicing elit, sed do eiusmod tempor incididunt ut labore et dolore magna aliqua. Lorem ipsum dolor sit amet, consectetur adipisicing elit, sed do eiusmod tempor incididunt ut labore et dolore magna aliqua. Lorem ipsum dolor sit amet, consectetur adipisicing elit, sed do eiusmod tempor incididunt ut labore et dolore magna aliqua. Lorem ipsum dolor sit amet, consectetur adipisicing elit, sed do eiusmod tempor incididunt ut labore et dolore magna aliqua. Lorem ipsum dolor sit amet, consectetur adipisicing elit, sed do eiusmod tempor incididunt ut labore et dolore magna aliqua.</p>
    <div class="meta"><span>3 days ago</span><span class="n"><i class="heart"></i>122<i class="bubble"></i>1</span></div>
  </article>
  <article class="card dl2">
    <div class="card-head"><h3>DOWNLOAD NOW</h3><i class="ico"></i></div>
    <div class="list">
      <div class="item"><span class="thumb" role="img" aria-label="Download thumbnail"></span><div><b>Aliquam congue</b>Fermentum nisl. Mauris accumsan nulla vel diam.</div></div>
      <div class="item"><span class="thumb alt" role="img" aria-label="Download thumbnail"></span><div><b>Aliquam congue</b>Fermentum nisl. Mauris accumsan nulla vel diam.</div></div>
      <div class="item"><span class="thumb" role="img" aria-label="Download thumbnail"></span><div><b>Aliquam congue</b>Fermentum nisl. Mauris accumsan nulla vel diam.</div></div>
      <div class="item"><span class="thumb alt" role="img" aria-label="Download thumbnail"></span><div><b>Aliquam congue</b>Fermentum nisl. Mauris accumsan nulla vel diam.</div></div>
      <div class="item"><span class="thumb" role="img" aria-label="Download thumbnail"></span><div><b>Aliquam congue</b>Fermentum nisl. Mauris accumsan nulla vel diam.</div></div>
      <div class="item"><span class="thumb alt" role="img" aria-label="Download thumbnail"></span><div><b>Aliquam congue</b>Fermentum nisl. Mauris accumsan nulla vel diam.</div></div>
    </div>
    <div class="meta"><span>3 days ago</span><span class="n"><i class="heart"></i>122<i class="bubble"></i>1</span></div>
  </article>
  <div class="more">LOAD MORE +</div>
</section>
</body>
</html>
```